BUSINESS CARD FOR GUITAR SCHOOL

I would like to design a business card for my Guitar Music School. The school is called "Pluck & Lantern".

The card should be yellow.

Target Market(s)

18-35 years old

Industry/Entity Type

School

Contact Information for Business Card

I would like to design a business card for my Guitar Music School. The school is called "Pluck & Lantern". The card should be yellow.

Card must be consistent with my website design: www.pluckandlantern.com.sg

Requirements
Must have
• 1) Name of Company
• 2) Company Logo
• 3) Name of Employee
• 4) Position of Employee
• 5) Contact Number
• 6) Address
Nice to have
• Creative Design
• Card must be consistent with my website design: www.pluckandlantern.com.sg
Should not have
• Boring Design

```html
<!DOCTYPE html>
<html lang="en">
<head>
<meta charset="utf-8">
<title>Pluck &amp; Lantern – Business Card</title>
<link rel="stylesheet" href="https://fonts.googleapis.com/css2?family=Poppins:wght@800&family=Open+Sans:wght@400;600;700&display=swap">
<style>
  :root {
    --backdrop: #e9e6e1;
    --card-black: #0b0b0b;
    --card-white: #ffffff;
    --brand-yellow: #f7d117;
    --brand-yellow-deep: #f2c200;
    --ink: #161616;
    --ink-soft: #555555;
  }
  * { box-sizing: border-box; margin: 0; padding: 0; }
  html, body {
    width: 1200px; height: 913px; overflow: hidden;
    background: var(--backdrop);
    font-family: "Open Sans", Arial, sans-serif;
  }
  .canvas {
    position: relative; width: 1200px; height: 913px;
    display: flex; align-items: center; justify-content: center; gap: 56px;
  }
  .card {
    position: relative; width: 532px; height: 304px;
    border-radius: 4px; overflow: hidden;
    box-shadow: 0 6px 18px rgba(0,0,0,.18);
  }

  /* Front */
  .card-front {
    background: var(--card-black);
    display: flex; flex-direction: column; align-items: center; justify-content: center;
  }
  .front-wordmark {
    font-family: "Poppins", Arial, sans-serif; font-weight: 800;
    font-size: 46px; line-height: 1; letter-spacing: -1px;
    color: var(--brand-yellow);
  }
  .front-tagline {
    margin-top: 10px; font-size: 14px; font-weight: 600;
    color: var(--brand-yellow);
  }

  /* Back */
  .card-back { background: var(--card-white); }
  .holder {
    position: absolute; right: 30px; top: 34px; text-align: right;
  }
  .holder-name { font-size: 16px; font-weight: 700; color: var(--ink); }
  .holder-role { font-size: 11px; color: var(--ink-soft); margin-top: 2px; }
  .divider {
    position: absolute; left: 30px; right: 150px; top: 78px;
    height: 2px; background: var(--brand-yellow);
  }
  .back-wordmark {
    position: absolute; left: 30px; top: 94px;
    font-family: "Poppins", Arial, sans-serif; font-weight: 800;
    font-size: 28px; line-height: 1; letter-spacing: -0.5px; color: var(--ink);
  }
  .back-tagline {
    position: absolute; left: 32px; top: 130px;
    font-size: 9.5px; font-weight: 600; color: var(--ink);
  }
  .divider-low {
    position: absolute; left: 30px; width: 210px; top: 156px;
    height: 2px; background: var(--brand-yellow);
  }
  .contact-list {
    position: absolute; left: 30px; top: 167px; list-style: none;
  }
  .contact-item {
    display: flex; align-items: center; gap: 10px;
    font-size: 12.5px; color: var(--ink); height: 20px;
  }
  .contact-icon { width: 12px; height: 12px; flex: none; }
  .address-band {
    position: absolute; left: 0; right: 0; bottom: 0; height: 64px;
    background: linear-gradient(180deg, var(--brand-yellow), var(--brand-yellow-deep));
    display: flex; align-items: center; padding-left: 30px;
    font-size: 13.5px; font-weight: 600; color: var(--ink);
  }
</style>
</head>
<body>
<main class="canvas">
  <section class="card card-front" aria-label="Business card front">
    <div class="front-wordmark">Pluck &amp; Lantern</div>
    <div class="front-tagline">Playing Guitar with Heart and Light</div>
  </section>

  <section class="card card-back" aria-label="Business card back">
    <div class="holder">
      <div class="holder-name">Your Long Name</div>
      <div class="holder-role">Managing Director</div>
    </div>
    <div class="divider"></div>
    <div class="back-wordmark">Pluck &amp; Lantern</div>
    <div class="back-tagline">Playing Guitar with Heart and Light</div>
    <div class="divider-low"></div>
    <ul class="contact-list">
      <li class="contact-item">
        <svg class="contact-icon" viewBox="0 0 24 24"><path fill="#161616" d="M6.6 10.8a15 15 0 0 0 6.6 6.6l2.2-2.2a1 1 0 0 1 1-.25 11.4 11.4 0 0 0 3.6.57 1 1 0 0 1 1 1V20a1 1 0 0 1-1 1A17 17 0 0 1 3 4a1 1 0 0 1 1-1h3.5a1 1 0 0 1 1 1c0 1.25.2 2.45.57 3.57a1 1 0 0 1-.25 1z"/></svg>
        <span>+65 91234567</span>
      </li>
      <li class="contact-item">
        <svg class="contact-icon" viewBox="0 0 24 24"><path d="M2 5h20v14H2z M2 5l10 8 10-8" fill="none" stroke="#161616" stroke-width="2.4"/></svg>
        <span>yourname@pluckandlantern.com.sg</span>
      </li>
      <li class="contact-item">
        <svg class="contact-icon" viewBox="0 0 24 24" fill="none" stroke="#161616" stroke-width="2.2"><circle cx="12" cy="12" r="10"/><path d="M2 12h20M12 2c3 3 3 17 0 20M12 2c-3 3-3 17 0 20"/></svg>
        <span>www.pluckandlantern.com.sg</span>
      </li>
    </ul>
    <div class="address-band">27 Kembangan Lane Orchid Building B #05-03 Singapore 418820</div>
  </section>
</main>
</body>
</html>
```